Successful Health Company Needs a Face Lift

We need a beautiful new design for our existing, online health supplements business.

Most of the elements are already there, but we need your sophistication and style.

The 3 pages that need your magic touch are:
Home page:
http://www.vitabrook.co.uk

Multiple Product pages. e.g:
http://www.vitabrook.co.uk/health-issues/major-organs/skin-hair-nails.html

Single Product pages. e.g:
http://www.vitabrook.co.uk/l-arginine-500-mg.html

Please have a look around.

This is a bilingual site, so all text (except logo) needs to be easily changed/translated. If photoshop files can be provided where we can simply translate the text layer of a graphic, that is acceptable. Please note that Greman words are generally longer than English.

Appearance:
The over all look should be open, light, uplifting and sophisticated.

The Home Page in detail:
We are largely happy with the category boxes in the centre column although you may restyle these if you wish.
The header, left menu and right column don't hang together and need your skills.

Logo:
We would like you to enhance our logo, but please note the 'S' and circle are used on many product labels, so we can't go too far from this just now.
(Product label example: http://www.vitabrook.co.uk/black-walnut-tincture-from-green-hull.html)

Header:
This needs to imply health and be light and stylish without it taking up valuable room.

Left Menu:
This is a multi-layer concertina menu. It is hard to see where your are within it. It needs to be made more clear and easy to navigate, maybe by using indentation and or better colour choices.
Please show it expanded and condensed in your design proposals.
(Extended menu example: http://www.vitabrook.co.uk/health-issues/female-health/thrush.html)

Multiple Product pages in detail
Please style the the brief descriptions, which must contain bullet points, price, add to basket and learn more.

Single Product pages in detail
The design and layout of this page needs to include all the elements currently there, including price, Qty, Add to Basket button, size and article number.

The static blocks on the right column will appear on these single product pages and need to suit the design well. They should not over-power the central content of the page.
Updates

Thank you all for participating.

Please note that what we are looking for is a more stylish and attractive version of what we already have.  The elements are all there.  We are not looking for a new concept.

We are happy for designers to switch images for better ones, work with colour ways, alter proportions and insert the elements in our brief.

We do not want to add banners, large images etc.  We want our customers to be familiar with what they see, and to be impressed with how much better the pages hang together.  They should not think they've landed at a new company.

We do want to see how the left menu looks when extended to show 2nd and 3rd tier menu titles.
We will also want to see how the design works for a multiple product page like this: http://www.vitabrook.co.uk/supplement-type/anti-microbials.html
as well as a single product page like this:  http://www.vitabrook.co.uk/black-walnut-extract.html

Some adjustment to the 'VitaBrook' logo is also an option and the graphic has been attached. 

Thank you for your careful attention to our brief.

Marcus.
pp Leopold

Project Deadline Extended
Reason: Due to unanticipated travel arrangements, the company director will only be available to make final decisions on Monday the 19th of March. Please continue updating submissions as we are in touch. Thank you for your understanding.

Target Market(s)

Health conscious women 70% men 30% aged 40 to 65 and health practitioners.

Industry/Entity Type

Health

Requirements
Must have
• Please include in the Header:
UK and German flags
Facebook, dig, +1, twitter, linked in, stumble upon
Padlock/SSL security/secure transaction
Practitioner helpline/ orders phone number
Paypal/Credit card logo

Please include in right column:
Clinician Corner
Mercury Free Dentistry
Shopping Basket
Storefronts for Therapists

Please include in either Header or Right Column
Same day dispatch
Money back warranty

```html
<!DOCTYPE html>
<html lang="en">
<head>
<meta charset="utf-8">
<title>VitaBrook Enterprises</title>
<link href="https://fonts.googleapis.com/css2?family=Noto+Sans+Mono:wght@400;500&family=Open+Sans:wght@400;600&family=Cousine:ital,wght@1,700&family=Kalam&display=swap" rel="stylesheet">
<style>
:root{
  --page:#e6e6e6;--card:#ffffff;--panel:#f3f3f3;
  --maroon:#8a1d3e;--ink:#2f2f2f;--muted:#666;
  --teal:#3fb8cf;--pink:#d2467c;--red:#d40000;--green:#6bb43a;
  --band-pink:#f6e4ec;--band-cyan:#dcf1f7;--band-green:#e6f4d7;
  --male:#2a8fb5;--news:#9fd3f3;--btn:#6d7680;
}
*{box-sizing:border-box;margin:0;padding:0}
html,body{width:1200px;height:1184px;overflow:hidden}
body{background:var(--page);position:relative;font-family:'Open Sans',sans-serif;color:var(--ink)}
.abs{position:absolute}
.card{position:absolute;background:var(--card);border-radius:4px;box-shadow:0 1px 4px rgba(0,0,0,.12)}
/* header */
.header{left:33px;top:12px;width:1138px;height:208px}
.logo{display:flex;align-items:center;gap:10px}
.logo-ring{width:72px;height:72px;border-radius:50%;border:7px solid var(--pink)}
.logo-name{color:var(--teal);font-weight:400;line-height:1}
.logo-name .big{font-size:33px;display:block;letter-spacing:1px}
.logo-name .small{font-size:11px;letter-spacing:3px;display:block;margin-top:8px;text-align:right}
.account{font-size:13px;color:#7a3440;white-space:nowrap}
.account span{margin-right:14px}
.flag{width:33px;height:17px}
.search{width:308px;height:27px;border:1px solid #ccc;border-radius:14px;background:#fafafa;font-size:11px;color:#999;font-style:italic;padding:6px 14px}
.search-btn{width:31px;height:27px;border-radius:0 14px 14px 0;background:var(--green)}
.phone-num{font-family:'Cousine',monospace;font-style:italic;font-weight:700;font-size:23px;color:var(--red);letter-spacing:1px;white-space:nowrap}
.nav{width:1101px;height:54px;background:linear-gradient(#fafafa,#ececec);border:1px solid #ddd}
.nav a{position:absolute;top:17px;font-size:14px;color:#555;text-decoration:none;white-space:nowrap}
.nav a.current{border-bottom:2px solid #777;padding:0 10px 4px}
.social{position:absolute;top:14px;width:29px;height:29px;border-radius:6px;background:linear-gradient(#5b9fd6,#2e6aa8)}
.cart-text{position:absolute;top:17px;font-size:14px;color:#444;white-space:nowrap}
/* categories */
.main{left:33px;top:231px;width:1138px;height:594px}
.panel{left:14px;top:15px;width:1117px;height:556px;background:var(--panel);border:1px solid #ddd;box-shadow:0 6px 8px -4px rgba(0,0,0,.2)}
.band{position:absolute;height:28px}
.band.pink{background:linear-gradient(90deg,var(--band-pink),#fff 60%,var(--band-pink))}
.band.cyan{background:linear-gradient(90deg,#fff,var(--band-cyan) 40%,#fff 70%,var(--band-cyan))}
.band.green{background:linear-gradient(90deg,var(--band-green),#fff 50%,var(--band-green))}
.cat-title{position:absolute;font-family:'Noto Sans Mono',monospace;font-weight:400;font-size:19px;color:var(--maroon);letter-spacing:.5px;white-space:nowrap}
.sub-title{position:absolute;font-family:'Noto Sans Mono',monospace;font-weight:400;font-size:16px;color:var(--maroon);white-space:nowrap}
.sub-title.male{color:var(--male)}
.photo{position:absolute;border:1px solid #ccc;border-radius:3px;box-shadow:0 1px 3px rgba(0,0,0,.15)}
.links{position:absolute;list-style:none}
.links li{height:25px;font-family:'Noto Sans Mono',monospace;font-size:12.5px;color:var(--ink);display:flex;align-items:center;gap:8px;white-space:nowrap}
.links.male li{color:var(--male)}
.dot{width:12px;height:12px;border-radius:50%;background:#fff;border:1px solid #ddd;color:var(--pink);font-size:10px;line-height:9px;text-align:center;flex:none}
.more{position:absolute;font-family:'Noto Sans Mono',monospace;font-size:12.5px;color:#1a237e}
/* footer */
.footer{left:33px;top:838px;width:1138px;height:346px}
.foot-panel{left:19px;top:19px;width:1099px;height:306px;background:#f5f5f5}
.foot-links{position:absolute;list-style:none}
.foot-links li{height:31px;border-bottom:1px solid #ddd;font-size:12.5px;display:flex;align-items:center;gap:12px;color:#222;white-space:nowrap}
.pract{left:494px;top:875px;width:210px;height:115px;border:1px solid #ccc;background:#fff}
.pract-head{height:28px;background:#9ef0ec;color:var(--pink);font-size:13px;padding:5px 20px;white-space:nowrap}
.pract-photo{left:0;top:28px;width:78px;height:86px;background:linear-gradient(#dfe9f2,#b7c9db)}
.pract-call{left:82px;top:36px;color:var(--pink);font-size:13px;line-height:17px;white-space:nowrap}
.pract-call .num{letter-spacing:1px}
.pract-call .or{font-size:10px;color:#aaa}
.pract-call .find{color:#2a5db0;text-decoration:underline;font-size:13px;letter-spacing:-.5px}
.webshop{left:719px;top:891px;width:208px;height:83px;background:#fff}
.webshop-hand{left:0;top:14px;width:62px;height:52px;background:linear-gradient(#f1cdb2,#d8a888);border-radius:20px 4px 4px 20px}
.webshop-title{left:60px;top:4px;font-size:22px;line-height:24px;color:var(--red);white-space:nowrap}
.webshop-sub{left:70px;top:30px;width:124px;font-family:'Kalam',cursive;font-size:18px;color:var(--red);line-height:21px;text-align:center;white-space:nowrap}
.partner{left:963px;top:894px;width:157px;height:75px;background:linear-gradient(#d7ecf9,#9fd0ef);border-bottom:4px solid #7cb342}
.newsletter{left:476px;top:996px;width:663px;height:60px;background:var(--news)}
.newsletter .label{position:absolute;left:34px;top:8px;font-size:31px;color:#fff;letter-spacing:1px}
.newsletter .field{position:absolute;left:227px;top:11px;width:243px;height:31px;background:#fff;border:1px solid #ccc}
.newsletter .btn{position:absolute;left:482px;top:10px;width:168px;height:33px;background:var(--btn);border:1px solid #555;color:#fff;font-size:18px;text-align:center;line-height:31px;border-radius:2px}
.rule{left:250px;top:1072px;width:735px;height:1px;background:linear-gradient(90deg,transparent,#9fd3f3,transparent)}
.legal{left:0;width:1200px;text-align:center;font-size:11px;color:#333}
.legal span{margin:0 7px}
</style>
</head>
<body>

<header class="card header">
  <div class="abs logo" style="left:43px;top:37px">
    <div class="logo-ring"></div>
    <div class="logo-name"><span class="big">VITABROOK</span><span class="small">ENTERPRISES</span></div>
  </div>
  <div class="abs account" style="left:761px;top:16px"><span>Welcome, ( Log in )</span><span>Your Account</span></div>
  <svg class="abs flag" style="left:1039px;top:19px" viewBox="0 0 33 17"><rect width="11" height="17" fill="#002b7f"/><rect x="11" width="11" height="17" fill="#fcd116"/><rect x="22" width="11" height="17" fill="#ce1126"/></svg>
  <svg class="abs flag" style="left:1080px;top:19px" viewBox="0 0 33 17"><rect width="33" height="17" fill="#012169"/><path d="M0 0L33 17M33 0L0 17" stroke="#fff" stroke-width="3"/><path d="M16.5 0V17M0 8.5H33" stroke="#fff" stroke-width="5"/><path d="M16.5 0V17M0 8.5H33" stroke="#c8102e" stroke-width="3"/></svg>
  <div class="abs search" style="left:762px;top:54px">search...</div>
  <svg class="abs search-btn" style="left:1039px;top:54px" viewBox="0 0 31 27"><circle cx="14" cy="12" r="5" fill="none" stroke="#fff" stroke-width="2"/><path d="M18 16l4 4" stroke="#fff" stroke-width="2.5"/></svg>
  <svg class="abs" style="left:757px;top:103px" width="34" height="40" viewBox="0 0 34 40"><path d="M8 3c-5 3-7 9-3 18s10 15 16 17c3 1 6-1 7-3l-6-6-4 3c-4-2-8-8-9-12l4-3-5-8z" fill="var(--red)"/></svg>
  <div class="abs phone-num" style="left:798px;top:112px">01632 960 418</div>
  <nav class="abs nav" style="left:19px;top:142px">
    <a class="current" style="left:26px">Home</a>
    <a style="left:123px">Detox</a>
    <a style="left:204px">Hydration</a>
    <a style="left:309px">Supplements</a>
    <a style="left:438px">Your Health Issues</a>
    <span class="social" style="left:659px"></span>
    <span class="social" style="left:701px"></span>
    <span class="social" style="left:747px"></span>
    <span class="social" style="left:792px;background:linear-gradient(#f1f6fb,#c9d9ea);border:1px solid #aac"></span>
    <svg class="abs" style="left:933px;top:8px" width="40" height="34" viewBox="0 0 40 34"><path d="M2 4h6l5 18h20l4-13H11" fill="none" stroke="var(--green)" stroke-width="3"/><circle cx="15" cy="28" r="3" fill="var(--green)"/><circle cx="30" cy="28" r="3" fill="var(--green)"/></svg>
    <span class="cart-text" style="left:983px">Cart: (empty)</span>
  </nav>
</header>

<main class="card main">
  <section class="abs panel">
    <div class="band pink" style="left:8px;top:14px;width:1095px"></div>
    <h2 class="cat-title" style="left:22px;top:16px">DIGESTION</h2>
    <h2 class="cat-title" style="left:405px;top:16px">PAIN</h2>
    <h2 class="cat-title" style="left:760px;top:16px">WEIGHT LOSS</h2>
    <div class="photo" role="img" aria-label="Hands cupped around a bare midriff" style="left:21px;top:58px;width:173px;height:115px;background:linear-gradient(135deg,#f3d9c4,#d9a98a 60%,#efe3dc)"></div>
    <ul class="links" style="left:211px;top:55px"><li><span class="dot">›</span>Colon Cleanse</li><li><span class="dot">›</span>Constipation</li><li><span class="dot">›</span>Candida</li><li><span class="dot">›</span>Irritable Bowel</li><li><span class="dot">›</span>Bloating &amp; Wind</li></ul>
    <div class="photo" role="img" aria-label="Man holding his aching lower back" style="left:397px;top:58px;width:177px;height:119px;background:linear-gradient(135deg,#d9d9d9,#8b8b8b 55%,#c8694f 70%,#eaeaea)"></div>
    <ul class="links" style="left:597px;top:53px"><li><span class="dot">›</span>Back Pain</li><li><span class="dot">›</span>Joint and Bone</li><li><span class="dot">›</span>Headaches</li><li><span class="dot">›</span>Period Pain</li></ul>
    <div class="photo" role="img" aria-label="Yellow tape measure around a slim waist" style="left:762px;top:57px;width:172px;height:120px;background:linear-gradient(90deg,#d59d74,#f4d37a 50%,#d59d74)"></div>
    <ul class="links" style="left:955px;top:56px"><li><span class="dot">›</span>Without Dieting</li><li><span class="dot">›</span>Supplements</li><li><span class="dot">›</span>Sugar Metabolism</li></ul>

    <div class="band cyan" style="left:8px;top:189px;width:1095px;height:30px"></div>
    <h2 class="cat-title" style="left:26px;top:190px">Health</h2>
    <h2 class="cat-title" style="left:652px;top:191px">Detox &amp; Cleansing</h2>
    <div class="photo" role="img" aria-label="Hands holding a red heart against blue sky" style="left:22px;top:233px;width:205px;height:118px;background:linear-gradient(135deg,#5fb7ea,#bfe3f7 45%,#d9262e 55%,#9fd3f3)"></div>
    <h3 class="sub-title" style="left:244px;top:240px">Female Health</h3>
    <ul class="links" style="left:248px;top:268px"><li><span class="dot">›</span>Breast Health</li><li><span class="dot">›</span>Menopause</li><li><span class="dot">›</span>Menstruation &amp; PMS</li></ul>
    <div class="abs" style="left:414px;top:232px;width:1px;height:122px;background:#ddd"></div>
    <h3 class="sub-title male" style="left:434px;top:240px">Mele Health</h3>
    <ul class="links male" style="left:428px;top:265px"><li><span class="dot">›</span>Erectile Dysfunction</li><li><span class="dot">›</span>Hair Loss</li><li><span class="dot">›</span>Prostate Health</li></ul>
    <div class="photo" role="img" aria-label="Pink lily, coconut and white towels" style="left:651px;top:230px;width:190px;height:122px;background:linear-gradient(135deg,#f6f6f6,#e9a7c3 40%,#9b6b4a 60%,#fafafa)"></div>
    <ul class="links" style="left:862px;top:231px"><li><span class="dot">›</span>Heavy Metal Detox</li><li><span class="dot">›</span>Parasite Cleanse</li><li><span class="dot">›</span>Kidney Cleanse</li><li><span class="dot">›</span>Liver Cleanse</li><li><span class="dot">›</span>Colon Cleanse</li></ul>

    <div class="band green" style="left:8px;top:369px;width:1095px"></div>
    <h2 class="cat-title" style="left:27px;top:371px">Body Care</h2>
    <h2 class="cat-title" style="left:298px;top:371px">Brain Health</h2>
    <h2 class="cat-title" style="left:619px;top:371px">Water &amp; Hydration</h2>
    <h2 class="cat-title" style="left:919px;top:371px">Health Devices</h2>
    <div class="photo" role="img" aria-label="Woman in white measuring her thigh" style="left:19px;top:404px;width:126px;height:122px;background:linear-gradient(135deg,#f8f1ec,#e6c2a9 55%,#f4f4f4)"></div>
    <ul class="links" style="left:162px;top:401px"><li><span class="dot">›</span>Anti Aging</li><li><span class="dot">›</span>Cosmetics</li><li><span class="dot">›</span>Skin Range</li><li><span class="dot">›</span>Face &amp; Mouth</li><li><span class="dot">›</span>Hair Care</li></ul>
    <div class="photo" role="img" aria-label="Blue brain illustration" style="left:299px;top:404px;width:120px;height:119px;background:radial-gradient(ellipse at 50% 45%,#3aa0dc 0 38%,#fff 40%)"></div>
    <ul class="links" style="left:438px;top:402px"><li><span class="dot">›</span>Memory</li><li><span class="dot">›</span>Headaches</li><li><span class="dot">›</span>Cognitive Function</li><li><span class="dot">›</span>Mood &amp; Sleep</li></ul>
    <div class="photo" role="img" aria-label="Splash of clear blue water" style="left:618px;top:405px;width:118px;height:118px;background:linear-gradient(#f4fbff,#a8d8f3 60%,#2c7fd0)"></div>
    <ul class="links" style="left:754px;top:408px"><li><span class="dot">›</span>Water Filtration</li><li><span class="dot">›</span>Electrolytes</li><li><span class="dot">›</span>Super-Hydration</li></ul>
    <div class="photo" role="img" aria-label="Stethoscope on a pale blue surface" style="left:922px;top:410px;width:165px;height:97px;background:linear-gradient(135deg,#eef3f8,#c3ccd6 50%,#4a4f58 75%,#e2e8ef)"></div>
    <span class="more" style="left:1052px;top:512px">More</span>
  </section>
</main>

<footer class="card footer">
  <div class="abs foot-panel"></div>
  <ul class="foot-links" style="left:31px;top:22px;width:200px">
    <li><span class="dot">›</span>Supplement Type Toggle</li><li><span class="dot">›</span>Your Health Issue Toggle</li><li><span class="dot">›</span>Expert Product Lines Toggle</li><li><span class="dot">›</span>Detox &amp; Cleansing Toggle</li><li><span class="dot">›</span>Water &amp; Hydration Toggle</li><li><span class="dot">›</span>Natural Body Care Toggle</li>
  </ul>
  <ul class="foot-links" style="left:253px;top:24px;width:165px">
    <li><span class="dot">›</span>Health Technology</li><li><span class="dot">›</span>Household Products</li><li><span class="dot">›</span>Laboratory Tests</li><li><span class="dot">›</span>Books &amp; Education</li><li><span class="dot">›</span>New &amp; Special Offers</li><li><span class="dot">›</span>Sport &amp; Fitness</li>
  </ul>
</footer>

<div class="abs pract">
  <div class="pract-head">PRACTITIONER HELP ?</div>
  <div class="abs pract-photo" role="img" aria-label="Smiling doctor in a white coat"></div>
  <div class="abs pract-call">PLEASE CALL:<br><span class="num">01632 960 418</span><br><span class="or">or</span> <span class="find">Find a Practitioner</span></div>
</div>

<div class="abs webshop">
  <div class="abs webshop-hand" role="img" aria-label="Hand pointing to the right"></div>
  <div class="abs webshop-title">Free Webshop</div>
  <div class="abs webshop-sub">for our<br>practitioners</div>
</div>

<div class="abs partner"></div>

<div class="abs newsletter">
  <span class="label">Newsletter</span>
  <span class="field"></span>
  <span class="btn">Subscribe</span>
</div>

<div class="abs rule"></div>
<p class="abs legal" style="top:1084px"><span>About Us</span><span>Search Terms</span><span>Advanced Search</span><span>Terms &amp; Conditions</span><span>Privacy Policy</span><span>Contact Us</span></p>
<p class="abs legal" style="top:1109px">© 2010 VitaBrook Enterprises. All Rights Reserved.</p>
<p class="abs legal" style="top:1134px;line-height:12px">Please note: This information is provided for educational purposes only. Medical advice is neither implied nor intended.<br>Please consult a health professional for medical advice.</p>

</body>
</html>
```